Flyer Designer for a Widow and Door Company - loooking for fresh design

We are looking for a flyer designed to advertise our business - we supply and install windows and doors - we are looking for a fresh looking flyer to distribute to drum up business - more information can be found at our website www.brightpanehouse.co.uk - We want a different approach than we currently have - making it vibrant and fresh - you can see the services on the website but its more the graphical design that we are looking for rather than content as the content from the website can be used for each service etc.

Target Market(s)

the general public

Colors

Designer to choose colors to be used in the design.

Requirements
Must have
• vibrant design and images

```html
<!DOCTYPE html>
<html lang="en">
<head>
<meta charset="utf-8">
<title>Bright Pane House – Flyer</title>
<link rel="stylesheet" href="https://fonts.googleapis.com/css2?family=Roboto+Condensed:wght@400;700&family=Open+Sans:wght@400;600;700&family=Arimo:wght@700&display=swap">
<style>
:root{
  --page-bg:#e4e4e4;
  --paper:#ffffff;
  --brand-blue:#2f74b5;
  --deep-blue:#1e56a8;
  --title-blue:#2e6fb5;
  --ink:#1d1d1d;
  --footer-grey:#7f7f80;
  --chip-grey:#c9c9cb;
  --hero-light:#f1f2f3;
  --hero-mid:#e2e4e7;
}
*{box-sizing:border-box;margin:0;padding:0}
html,body{width:1200px;height:1200px;overflow:hidden;background:var(--page-bg)}
.flyer{
  position:absolute;left:187px;top:20px;width:929px;height:1303px;
  background:var(--paper);transform:scale(0.89);transform-origin:0 0;
  font-family:"Open Sans",sans-serif;color:var(--ink);overflow:hidden;
}
/* brand */
.brand{position:absolute;left:322px;top:44px;display:flex;align-items:center;gap:12px}
.brand-mark{width:58px;height:74px;background:var(--deep-blue)}
.brand-text{display:flex;flex-direction:column;gap:4px}
.brand-name{font-family:"Open Sans",sans-serif;font-weight:700;font-size:27px;color:var(--deep-blue);letter-spacing:.5px;line-height:1}
.brand-tag{font-family:"Open Sans",sans-serif;font-weight:700;font-size:11px;color:var(--deep-blue);letter-spacing:.4px}
/* hero */
.hero{position:absolute;left:0;top:130px;width:929px;height:332px;
  background:linear-gradient(90deg,var(--hero-mid) 0%,var(--hero-light) 45%,var(--hero-mid) 100%)}
.hero-art{position:absolute;left:0;top:0;width:300px;height:332px;
  background:linear-gradient(180deg,#d9dcdf 0%,#c6cbcf 60%,#8fae6a 100%)}
.headline{position:absolute;left:326px;top:242px;font-family:"Roboto Condensed",sans-serif;font-weight:700;
  font-size:55px;line-height:66px;color:var(--title-blue);text-transform:uppercase;letter-spacing:-.3px}
/* services column */
.services{position:absolute;left:28px;top:462px;width:492px;height:841px;background:var(--brand-blue)}
.service{position:absolute;left:0;width:492px}
.service-head{position:relative;height:60px}
.service-icon{position:absolute;left:20px;top:0;width:70px;height:60px;background:var(--chip-grey);
  clip-path:polygon(14% 0,86% 0,100% 50%,86% 100%,14% 100%,0 50%)}
.service-icon .tile{position:absolute;left:14px;top:0;width:42px;height:60px;background:#fff}
.service-icon svg{position:absolute;left:17px;top:12px}
.service-head .bar{position:absolute;left:0;top:28px;width:22px;height:4px;background:var(--chip-grey)}
.service-title{position:absolute;left:88px;top:14px;height:33px;padding:0 28px 0 26px;background:#fff;border-radius:0 17px 17px 0;
  font-family:"Arimo",sans-serif;font-weight:700;font-size:24px;line-height:33px;color:var(--deep-blue)}
.service-body{margin:14px 32px 0 28px;color:#fff;font-size:15px;line-height:22px;text-align:justify}
.service-body p+p{margin-top:5px}
/* benefits column */
.intro{position:absolute;left:554px;top:476px;width:346px;font-size:15px;line-height:22px;font-weight:600;text-align:justify;color:var(--ink)}
.benefit{position:absolute;left:566px;width:340px}
.benefit-icon{position:absolute;left:0;top:-2px;width:34px;height:26px}
.benefit-title{margin-left:48px;font-family:"Roboto Condensed",sans-serif;font-weight:700;font-size:18px;line-height:20px;color:var(--title-blue);text-transform:uppercase}
.benefit-desc{margin-left:48px;margin-top:3px;font-size:15px;line-height:19px;color:var(--ink);width:290px}
.badge{position:absolute;left:-32px;top:2px;width:74px;height:12px;background:var(--deep-blue);border-radius:2px}
/* footer */
.footer{position:absolute;left:0;top:1215px;width:929px;height:61px;background:var(--footer-grey);color:#fff;
  font-family:"Roboto Condensed",sans-serif}
.contact{position:absolute;top:0;height:61px;display:flex;align-items:center;gap:12px;font-size:18px}
.contact.phone{left:42px;font-weight:700;font-size:20px}
.contact.mail{left:294px}
.contact.web{left:632px}
.under-strip{position:absolute;left:28px;top:1276px;width:492px;height:27px;background:var(--brand-blue)}
</style>
</head>
<body>
<main class="flyer">
  <header class="brand">
    <div class="brand-mark"></div>
    <div class="brand-text">
      <span class="brand-name">BRIGHT PANE HOUSE LTD</span>
      <span class="brand-tag">BESPOKE WINDOWS &amp; DOORS</span>
    </div>
  </header>

  <section class="hero">
    <div class="hero-art" role="img" aria-label="Illustration of a dark front door with a fanlight, wall lanterns and topiary plants against white weatherboard cladding"></div>
  </section>
  <h1 class="headline">For extra security<br>and your piece of mind</h1>

  <section class="services">
    <article class="service" style="top:17px">
      <div class="service-head"><span class="bar"></span>
        <div class="service-icon"><div class="tile"></div>
          <svg width="36" height="36" viewBox="0 0 36 36"><rect x="6" y="2" width="24" height="32" fill="none" stroke="#1e56a8" stroke-width="3"/><path d="M6 13h24M6 23h24M14 2v32M22 2v32" stroke="#1e56a8" stroke-width="2"/></svg></div>
        <h2 class="service-title">OUR WINDOWS</h2></div>
      <div class="service-body"><p>Our windows are individually designed to suit your home. Bespoke to your individual requirements.</p>
        <p>Our windows offer an excepional level of energy efficency with market leading locking systems.</p></div>
    </article>
    <article class="service" style="top:213px">
      <div class="service-head"><span class="bar"></span>
        <div class="service-icon"><div class="tile"></div>
          <svg width="36" height="36" viewBox="0 0 36 36"><rect x="8" y="3" width="20" height="30" fill="none" stroke="#1e56a8" stroke-width="3"/><path d="M8 3l10 4v29l-10-3z" fill="#1e56a8"/><circle cx="16" cy="19" r="1.5" fill="#fff"/></svg></div>
        <h2 class="service-title">REPAIRS</h2></div>
      <div class="service-body"><p>At the Bright Pane House we offer a full repair and replacement service on glass units, windows and doors. No job is too small. Please contact one of our helpful advisors for a non obligatory quotation or to learn more please click the link below.</p></div>
    </article>
    <article class="service" style="top:422px">
      <div class="service-head"><span class="bar"></span>
        <div class="service-icon"><div class="tile"></div>
          <svg width="36" height="36" viewBox="0 0 36 36"><path d="M6 30L24 12M28 4a6 6 0 0 0-6 8l2 2a6 6 0 0 0 8-6l-4 2-2-2z" stroke="#1e56a8" stroke-width="4" fill="#1e56a8" stroke-linecap="round"/><path d="M8 6l22 24" stroke="#1e56a8" stroke-width="5" stroke-linecap="round"/></svg></div>
        <h2 class="service-title">OUR DOORS</h2></div>
      <div class="service-body"><p>A new door from Bright Pane House can transform the look of your home, offer increased thermal efficiency and dramatically improve security for your peace of mind.</p></div>
    </article>
    <article class="service" style="top:588px">
      <div class="service-head"><span class="bar"></span>
        <div class="service-icon"><div class="tile"></div>
          <svg width="36" height="36" viewBox="0 0 36 36"><path d="M4 14L20 4l12 8v14H14l-8 8v-8H4z" fill="#1e56a8"/></svg></div>
        <h2 class="service-title">LANDLORD SERVICES</h2></div>
      <div class="service-body"><p>We work closely with Landlords &amp; Letting Agents to offer a full repair or replacement service on glass units, windows and doors as well as adjustments and replacement or repair of hinges, handles locks and cylinders.</p></div>
    </article>
  </section>

  <p class="intro">At the Bright Pane House we offer the following benefits as standard on all of our products for your peace of mind -</p>

  <div class="benefit" style="top:570px"><span class="badge"></span>
    <h3 class="benefit-title">Registered Installer</h3><p class="benefit-desc">Accredited and fully Compliant with all carrent regulations</p></div>
  <div class="benefit" style="top:656px">
    <svg class="benefit-icon" viewBox="0 0 34 26"><path d="M11 11V7a6 6 0 0 1 12 0v4" fill="none" stroke="#1e56a8" stroke-width="2.5"/><rect x="8" y="11" width="18" height="14" rx="2" fill="#f2b705"/></svg>
    <h3 class="benefit-title">UK Made</h3><p class="benefit-desc">Proudly Made in the United Kingdom</p></div>
  <div class="benefit" style="top:722px">
    <svg class="benefit-icon" viewBox="0 0 34 26"><path d="M4 24V12L16 3l14 9v12z" fill="none" stroke="#444" stroke-width="2"/><rect x="14" y="14" width="14" height="10" fill="#7bb23a"/></svg>
    <h3 class="benefit-title">10 Year Guarantee</h3><p class="benefit-desc">For your peace of mind</p></div>
  <div class="benefit" style="top:788px">
    <svg class="benefit-icon" viewBox="0 0 34 26"><rect x="3" y="4" width="28" height="18" fill="#1e3f8a"/><path d="M3 4l28 18M31 4L3 22" stroke="#fff" stroke-width="4"/><path d="M17 4v18M3 13h28" stroke="#fff" stroke-width="6"/><path d="M17 4v18M3 13h28" stroke="#d3202f" stroke-width="3"/></svg>
    <h3 class="benefit-title">Additonal Security</h3><p class="benefit-desc" style="line-height:18px">all feature multipoint locking system for security and peace of mind</p></div>
  <div class="benefit" style="top:877px">
    <svg class="benefit-icon" viewBox="0 0 34 26"><circle cx="13" cy="13" r="10" fill="#e5e5e5" stroke="#555" stroke-width="2"/><path d="M20 18l12 6" stroke="#e8b90b" stroke-width="3"/></svg>
    <h3 class="benefit-title">Precision Made to Measure</h3><p class="benefit-desc">Bespokely made to your specification</p></div>
  <div class="benefit" style="top:943px">
    <svg class="benefit-icon" viewBox="0 0 34 26"><circle cx="17" cy="13" r="12" fill="#c8202a" stroke="#333" stroke-width="2"/></svg>
    <h3 class="benefit-title">Friendly Professional Staff</h3><p class="benefit-desc">We bring you the personal touch</p></div>
  <div class="benefit" style="top:1012px">
    <svg class="benefit-icon" viewBox="0 0 34 26"><rect x="6" y="1" width="22" height="24" fill="#fbe7c6" stroke="#d28a16" stroke-width="2"/><rect x="10" y="6" width="14" height="10" fill="#d28a16"/></svg>
    <h3 class="benefit-title">A Rated Energy Efficient</h3><p class="benefit-desc" style="line-height:18px;text-align:justify">Ensures Minimum heat loss with maximum heat retention</p></div>
  <div class="benefit" style="top:1099px">
    <svg class="benefit-icon" viewBox="0 0 34 26"><circle cx="22" cy="4" r="3" fill="#c8202a"/><path d="M21 8l-4 8 6 4-2 6M17 16l-8 2M20 10l8 4" stroke="#222" stroke-width="3" fill="none" stroke-linecap="round"/></svg>
    <h3 class="benefit-title">Competitive Pricing</h3><p class="benefit-desc">No Hidden Costs</p></div>
  <div class="benefit" style="top:1167px">
    <svg class="benefit-icon" viewBox="0 0 34 26"><rect x="5" y="4" width="22" height="20" fill="#f4f4f4" stroke="#aaa" stroke-width="1.5"/><path d="M12 16l5 4L31 2" stroke="#e3a31b" stroke-width="2.5" fill="none"/></svg>
    <h3 class="benefit-title">No Obligation Quotes</h3><p class="benefit-desc">No high Pressure Sales tactics</p></div>

  <footer class="footer">
    <div class="contact phone">
      <svg width="16" height="26" viewBox="0 0 16 26"><path d="M5 2h3l1 6-3 2c0 3 1 6 3 8l3-1 2 5-3 2C5 24 2 16 3 6z" fill="none" stroke="#fff" stroke-width="1.8"/></svg>
      <span>01632 960 418</span></div>
    <div class="contact mail">
      <svg width="30" height="18" viewBox="0 0 30 18"><rect x="1" y="1" width="28" height="16" fill="none" stroke="#fff" stroke-width="1.8"/><path d="M1 1l14 10L29 1M1 17l10-8M29 17l-10-8" fill="none" stroke="#fff" stroke-width="1.5"/></svg>
      <span>sales@brightpanehouse.co.uk</span></div>
    <div class="contact web">
      <svg width="24" height="24" viewBox="0 0 24 24"><circle cx="12" cy="12" r="10" fill="none" stroke="#fff" stroke-width="1.8"/><ellipse cx="12" cy="12" rx="4.5" ry="10" fill="none" stroke="#fff" stroke-width="1.5"/><path d="M2 12h20M4 6h16M4 18h16" stroke="#fff" stroke-width="1.5"/></svg>
      <span>www.brightpanehouse.co.uk</span></div>
  </footer>
  <div class="under-strip"></div>
</main>
</body>
</html>
```